Webdesign für Onlineshop für hochwertige Porzellan- und Glaswaren
Zielgruppe
Es soll einer neuer Onlineshop für hochwertige Porzellan- und Glaswaren entstehen.
Aufgabenstellung
Logo ist bereits vorhanden. Es soll ein hochwertiges und dennoch übersichtliches Design erstellt werden.
Anbei einige Referenzen:
https://www.velumora.com/
https://www.kandrivel.de/en-de/
https://pemoxa.it/en/home-page/

```html
<!DOCTYPE html>
<html lang="de">
<head>
<meta charset="utf-8">
<title>Produkte – Ceravel</title>
<link href="https://fonts.googleapis.com/css2?family=Lato:ital,wght@0,300;0,400;0,700;1,400&family=Playfair+Display:wght@700;900&display=swap" rel="stylesheet">
<style>
:root{
  --navy:#2c2f7a;
  --sky:#a9c4f5;
  --paper:#efeeec;
  --white:#ffffff;
  --ink:#3a3a3a;
  --muted:#7b7b7b;
  --sale:#f0136a;
  --stock:#5aa83c;
}
*{box-sizing:border-box;margin:0;padding:0}
html,body{width:763px;height:1200px;overflow:hidden}
body{position:relative;font-family:'Lato',sans-serif;color:var(--ink);background:var(--paper)}
.abs{position:absolute}
.serif{font-family:'Playfair Display',serif}

/* header */
.site-header{position:absolute;left:0;top:0;width:763px;height:44px;background:var(--paper)}
.main-nav a{position:absolute;top:17px;font-size:7px;color:var(--muted);text-decoration:none;font-weight:300}
.main-nav a.active{color:var(--navy);font-weight:700}
.search{position:absolute;left:527px;top:16px;width:113px;height:13px;border-bottom:1px solid var(--navy);font-size:5px;font-style:italic;color:var(--muted);padding-top:3px}
.accent-band{position:absolute;left:0;top:44px;width:763px;height:4px;background:var(--sky)}

/* hero */
.hero{position:absolute;left:0;top:48px;width:763px;height:175px;background:radial-gradient(ellipse at 30% 55%,#5a5a5a 0%,#2a2a2a 45%,#111 100%)}
.hero h1{position:absolute;left:0;width:763px;top:50px;text-align:center;color:#fff;font-family:'Playfair Display',serif;font-size:24px;font-weight:700}
.hero .sub{position:absolute;left:0;width:763px;top:76px;text-align:center;color:#eee;font-size:10px;font-weight:300}
.pill{position:absolute;top:104px;height:18px;border:1px solid var(--sky);border-radius:9px;color:var(--sky);font-size:7px;font-weight:700;display:flex;align-items:center;justify-content:center}
.pill.active{background:var(--sky);color:#fff}
.more{position:absolute;left:0;width:763px;top:139px;text-align:center;color:#fff;font-size:8px;font-weight:700;text-decoration:underline}

/* filters */
.filter-bar{position:absolute;left:0;top:223px;width:763px;height:37px;background:var(--white)}
.select{position:absolute;top:10px;height:20px;border:1px solid var(--navy);font-size:8px;color:var(--navy);padding:5px 9px}
.select svg{position:absolute;right:8px;top:7px}
.filter-link{position:absolute;top:15px;font-size:8px;color:#8a8fc0;font-weight:300}
.count{position:absolute;right:73px;top:266px;font-size:6px;font-style:italic;color:var(--navy)}

/* products */
.card{position:absolute;width:147px;height:196px;background:var(--white)}
.card .thumb{position:absolute;left:36px;top:20px;width:74px;height:74px;border-radius:50%}
.card .fav{position:absolute;right:13px;top:11px}
.badge{position:absolute;left:7px;top:0;height:14px;padding:0 8px;font-size:7px;color:#fff;display:flex;align-items:center;background:var(--sky)}
.badge.sale{background:var(--sale)}
.brand{position:absolute;left:11px;top:108px;font-size:7px;color:var(--muted);font-weight:300}
.name{position:absolute;left:10px;top:120px;width:130px;font-size:7px;line-height:9px;color:var(--ink)}
.stock{position:absolute;left:11px;top:148px;font-size:6px;color:var(--stock);display:flex;gap:4px;align-items:center}
.price{position:absolute;left:11px;top:166px;font-family:'Playfair Display',serif;font-weight:900;font-size:12px;color:var(--navy)}
.price.sale{color:var(--sale)}
.price s{font-family:'Lato',sans-serif;font-weight:400;font-size:5px;color:var(--muted);margin-left:6px;vertical-align:middle}
.cart-btn{position:absolute;left:114px;top:162px;width:22px;height:22px;border-radius:50%;background:var(--navy);display:flex;align-items:center;justify-content:center}

/* pagination */
.pager{position:absolute;left:0;top:915px;width:763px;height:50px;background:var(--white);display:flex;justify-content:center;align-items:center;gap:7px;font-size:8px;color:var(--navy)}
.pager .num{width:12px;height:12px;display:flex;align-items:center;justify-content:center}
.pager .current{background:var(--sky);color:#fff;border-radius:50%}

/* footer */
.footer-ornament{position:absolute;left:630px;top:1030px;width:133px;height:138px;background:radial-gradient(circle at 70% 40%,rgba(169,196,245,.45),rgba(169,196,245,0) 70%)}
.newsletter-kicker{position:absolute;left:72px;top:1006px;font-size:9px;font-weight:300;color:var(--muted)}
.newsletter-title{position:absolute;left:72px;top:1026px;font-family:'Playfair Display',serif;font-weight:700;font-size:19px;color:#555}
.newsletter-text{position:absolute;left:72px;top:1060px;width:190px;font-size:10px;line-height:12px;color:#555}
.email{position:absolute;left:72px;top:1092px;width:115px;height:29px;background:#fff;font-size:5.5px;font-style:italic;color:var(--muted);padding:12px 9px}
.signup{position:absolute;left:188px;top:1092px;width:71px;height:29px;background:var(--navy);color:#fff;font-size:10px;font-weight:300;display:flex;align-items:center;justify-content:center}
.foot-col{position:absolute;top:1006px}
.foot-col h3{font-family:'Playfair Display',serif;font-weight:700;font-size:10px;color:#555;margin-bottom:7px}
.foot-col li{list-style:none;font-size:7px;line-height:16px;color:#555}
.brand-mark{position:absolute;left:560px;top:1038px;width:130px;text-align:center;font-family:'Playfair Display',serif;font-weight:700;font-size:19px;letter-spacing:1px;color:var(--navy)}
.brand-dot{position:absolute;left:606px;top:1005px;width:28px;height:28px;border-radius:50%;background:var(--navy)}
.usp-band{position:absolute;left:0;top:1168px;width:763px;height:24px;background:var(--sky);font-size:7px;font-weight:300;color:#4a4f8a}
.usp-band span{position:absolute;top:8px}
.bottom-bar{position:absolute;left:0;top:1192px;width:763px;height:8px;background:var(--navy)}
</style>
</head>
<body>

<header class="site-header">
  <nav class="main-nav">
    <a style="left:140px">Home</a>
    <a style="left:187px">Kollektionen</a>
    <a style="left:253px">Neuheiten</a>
    <a class="active" style="left:312px">Produkte</a>
    <a style="left:367px">Inspiration</a>
  </nav>
  <div class="search">Suche...</div>
  <svg class="abs" style="left:630px;top:15px" width="10" height="10" viewBox="0 0 10 10"><circle cx="4" cy="4" r="3.2" fill="none" stroke="#333" stroke-width="1"/><line x1="6.3" y1="6.3" x2="9.3" y2="9.3" stroke="#333" stroke-width="1"/></svg>
  <svg class="abs" style="left:650px;top:15px" width="15" height="13" viewBox="0 0 24 21"><path d="M12 20 L2.5 10.5 A5.5 5.5 0 0 1 12 3.5 A5.5 5.5 0 0 1 21.5 10.5 Z" fill="none" stroke="#222" stroke-width="1.8"/></svg>
  <svg class="abs" style="left:672px;top:14px" width="16" height="15" viewBox="0 0 24 22"><path d="M1 2h4l3 12h12l2-8H7" fill="none" stroke="#222" stroke-width="1.8"/><line x1="8" y1="10" x2="21" y2="10" stroke="#222" stroke-width="1.4"/><circle cx="10" cy="19" r="1.8" fill="#222"/><circle cx="18" cy="19" r="1.8" fill="#222"/></svg>
</header>
<div class="accent-band"></div>

<section class="hero" role="img" aria-label="Dunkles Foto grober Keramikschalen">
  <h1>Produkte</h1>
  <div class="sub">Was suchen Sie?</div>
  <div class="pill" style="left:180px;width:51px">Vasen</div>
  <div class="pill" style="left:235px;width:63px">Geschenke</div>
  <div class="pill" style="left:303px;width:63px">Accessoires</div>
  <div class="pill active" style="left:372px;width:63px">Teller</div>
  <div class="pill" style="left:441px;width:63px">Weingläser</div>
  <div class="pill" style="left:509px;width:63px">Platten</div>
  <div class="more">Mehr Optionen</div>
</section>

<div class="filter-bar">
  <div class="select" style="left:72px;width:89px">Kollektion<svg width="8" height="5" viewBox="0 0 8 5"><path d="M1 1l3 3 3-3" fill="none" stroke="#2c2f7a" stroke-width="1"/></svg></div>
  <div class="select" style="left:165px;width:90px">Farbe<svg width="8" height="5" viewBox="0 0 8 5"><path d="M1 1l3 3 3-3" fill="none" stroke="#2c2f7a" stroke-width="1"/></svg></div>
  <div class="select" style="left:259px;width:90px">Dekor<svg width="8" height="5" viewBox="0 0 8 5"><path d="M1 1l3 3 3-3" fill="none" stroke="#2c2f7a" stroke-width="1"/></svg></div>
  <div class="filter-link" style="left:360px">Mehr Filter
    <svg width="9" height="8" viewBox="0 0 9 8" style="vertical-align:middle"><path d="M0.5 0.5h8L5.5 4v3.5L3.5 6.5V4z" fill="none" stroke="#2c2f7a" stroke-width=".8"/></svg></div>
  <div class="filter-link" style="left:560px">Sortierung</div>
  <div class="select" style="left:601px;width:90px">meistverkauft<svg width="8" height="5" viewBox="0 0 8 5"><path d="M1 1l3 3 3-3" fill="none" stroke="#2c2f7a" stroke-width="1"/></svg></div>
</div>

<div class="count">2.586 Ergebnisse</div>

<main>
  <!-- row 1 -->
  <article class="card" style="left:72px;top:284px">
    <div class="thumb" role="img" aria-label="Beiger Dessertteller mit grüngrauem Spiegel" style="background:radial-gradient(circle,#a9ad9c 20%,#d8cdb5 60%,#e6dcc6)"></div>
    <div class="badge">NEU</div>
    <svg class="fav" width="14" height="12" viewBox="0 0 24 21"><path d="M12 20 L2.5 10.5 A5.5 5.5 0 0 1 12 3.5 A5.5 5.5 0 0 1 21.5 10.5 Z" fill="none" stroke="#333" stroke-width="1.5"/></svg>
    <div class="brand">LOREVA</div>
    <div class="name">Dessertteller NATURE COLLECTION (6 Stck.), ⌀21 cm</div>
    <div class="stock"><svg width="10" height="6" viewBox="0 0 10 6"><rect x="0" y="1" width="6" height="3.5" fill="none" stroke="#5aa83c" stroke-width=".8"/><path d="M6 2h2l1.5 1.5V4.5H6z" fill="#5aa83c"/><circle cx="2" cy="5.2" r=".8" fill="#5aa83c"/><circle cx="7.5" cy="5.2" r=".8" fill="#5aa83c"/></svg>Auf Lager</div>
    <div class="price">24,95 €</div>
    <div class="cart-btn"><svg width="11" height="10" viewBox="0 0 11 10"><path d="M0.5 1h2l1.5 5.5h5.5l1-4H3" fill="none" stroke="#fff" stroke-width="1"/><path d="M6.5 2v3M5 3.5h3" stroke="#fff" stroke-width=".9"/><circle cx="4.5" cy="8.5" r=".9" fill="#fff"/><circle cx="8.5" cy="8.5" r=".9" fill="#fff"/></svg></div>
  </article>

  <article class="card" style="left:229px;top:284px">
    <div class="thumb" role="img" aria-label="Dunkelblauer Dessertteller" style="background:radial-gradient(circle,#3a5296 30%,#253a78 80%,#1b2b5e)"></div>
    <svg class="fav" width="14" height="12" viewBox="0 0 24 21"><path d="M12 20 L2.5 10.5 A5.5 5.5 0 0 1 12 3.5 A5.5 5.5 0 0 1 21.5 10.5 Z" fill="none" stroke="#333" stroke-width="1.5"/></svg>
    <div class="brand">LOREVA</div>
    <div class="name">Dessertteller NATURE COLLECTION (6 Stck.), ⌀21 cm</div>
    <div class="stock"><svg width="10" height="6" viewBox="0 0 10 6"><rect x="0" y="1" width="6" height="3.5" fill="none" stroke="#5aa83c" stroke-width=".8"/><path d="M6 2h2l1.5 1.5V4.5H6z" fill="#5aa83c"/><circle cx="2" cy="5.2" r=".8" fill="#5aa83c"/><circle cx="7.5" cy="5.2" r=".8" fill="#5aa83c"/></svg>Auf Lager</div>
    <div class="price">24,95 €</div>
    <div class="cart-btn"><svg width="11" height="10" viewBox="0 0 11 10"><path d="M0.5 1h2l1.5 5.5h5.5l1-4H3" fill="none" stroke="#fff" stroke-width="1"/><path d="M6.5 2v3M5 3.5h3" stroke="#fff" stroke-width=".9"/><circle cx="4.5" cy="8.5" r=".9" fill="#fff"/><circle cx="8.5" cy="8.5" r=".9" fill="#fff"/></svg></div>
  </article>

  <article class="card" style="left:386px;top:284px">
    <div class="thumb" role="img" aria-label="Gestapeltes petrolfarbenes Teller- und Schalenset" style="border-radius:40%;background:radial-gradient(ellipse,#4f8783 30%,#3b6a67 70%,#fff 72%)"></div>
    <svg class="fav" width="14" height="12" viewBox="0 0 24 21"><path d="M12 20 L2.5 10.5 A5.5 5.5 0 0 1 12 3.5 A5.5 5.5 0 0 1 21.5 10.5 Z" fill="none" stroke="#333" stroke-width="1.5"/></svg>
    <div class="brand">TIDEMOOR</div>
    <div class="name">Dessert Teller Set NATURE COLLECTION (6 Stck.), ⌀21 cm</div>
    <div class="stock"><svg width="10" height="6" viewBox="0 0 10 6"><rect x="0" y="1" width="6" height="3.5" fill="none" stroke="#5aa83c" stroke-width=".8"/><path d="M6 2h2l1.5 1.5V4.5H6z" fill="#5aa83c"/><circle cx="2" cy="5.2" r=".8" fill="#5aa83c"/><circle cx="7.5" cy="5.2" r=".8" fill="#5aa83c"/></svg>Auf Lager</div>
    <div class="price">24,95 €</div>
    <div class="cart-btn"><svg width="11" height="10" viewBox="0 0 11 10"><path d="M0.5 1h2l1.5 5.5h5.5l1-4H3" fill="none" stroke="#fff" stroke-width="1"/><path d="M6.5 2v3M5 3.5h3" stroke="#fff" stroke-width=".9"/><circle cx="4.5" cy="8.5" r=".9" fill="#fff"/><circle cx="8.5" cy="8.5" r=".9" fill="#fff"/></svg></div>
  </article>

  <article class="card" style="left:543px;top:284px">
    <div class="thumb" role="img" aria-label="Petrolfarbener Teller mit braunem Rand" style="width:68px;height:68px;left:39px;top:23px;background:radial-gradient(circle,#5a8284 40%,#40666a 85%,#8a5a35)"></div>
    <svg class="fav" width="14" height="12" viewBox="0 0 24 21"><path d="M12 20 L2.5 10.5 A5.5 5.5 0 0 1 12 3.5 A5.5 5.5 0 0 1 21.5 10.5 Z" fill="none" stroke="#333" stroke-width="1.5"/></svg>
    <div class="brand">TIDEMOOR</div>
    <div class="name">Dessertteller HANDMADE, glasiert, ⌀21 cm</div>
    <div class="stock"><svg width="10" height="6" viewBox="0 0 10 6"><rect x="0" y="1" width="6" height="3.5" fill="none" stroke="#5aa83c" stroke-width=".8"/><path d="M6 2h2l1.5 1.5V4.5H6z" fill="#5aa83c"/><circle cx="2" cy="5.2" r=".8" fill="#5aa83c"/><circle cx="7.5" cy="5.2" r=".8" fill="#5aa83c"/></svg>Auf Lager</div>
    <div class="price">24,95 €</div>
    <div class="cart-btn"><svg width="11" height="10" viewBox="0 0 11 10"><path d="M0.5 1h2l1.5 5.5h5.5l1-4H3" fill="none" stroke="#fff" stroke-width="1"/><path d="M6.5 2v3M5 3.5h3" stroke="#fff" stroke-width=".9"/><circle cx="4.5" cy="8.5" r=".9" fill="#fff"/><circle cx="8.5" cy="8.5" r=".9" fill="#fff"/></svg></div>
  </article>

  <!-- row 2 -->
  <article class="card" style="left:72px;top:490px">
    <div class="thumb" role="img" aria-label="Dunkelblauer Dessertteller" style="background:radial-gradient(circle,#3a5296 30%,#253a78 80%,#1b2b5e)"></div>
    <svg class="fav" width="14" height="12" viewBox="0 0 24 21"><path d="M12 20 L2.5 10.5 A5.5 5.5 0 0 1 12 3.5 A5.5 5.5 0 0 1 21.5 10.5 Z" fill="none" stroke="#333" stroke-width="1.5"/></svg>
    <div class="brand">LOREVA</div>
    <div class="name">Dessertteller NATURE COLLECTION (6 Stck.), ⌀21 cm</div>
    <div class="stock"><svg width="10" height="6" viewBox="0 0 10 6"><rect x="0" y="1" width="6" height="3.5" fill="none" stroke="#5aa83c" stroke-width=".8"/><path d="M6 2h2l1.5 1.5V4.5H6z" fill="#5aa83c"/><circle cx="2" cy="5.2" r=".8" fill="#5aa83c"/><circle cx="7.5" cy="5.2" r=".8" fill="#5aa83c"/></svg>Auf Lager</div>
    <div class="price">24,95 €</div>
    <div class="cart-btn"><svg width="11" height="10" viewBox="0 0 11 10"><path d="M0.5 1h2l1.5 5.5h5.5l1-4H3" fill="none" stroke="#fff" stroke-width="1"/><path d="M6.5 2v3M5 3.5h3" stroke="#fff" stroke-width=".9"/><circle cx="4.5" cy="8.5" r=".9" fill="#fff"/><circle cx="8.5" cy="8.5" r=".9" fill="#fff"/></svg></div>
  </article>

  <article class="card" style="left:229px;top:490px">
    <div class="thumb" role="img" aria-label="Beiger Dessertteller mit grüngrauem Spiegel" style="background:radial-gradient(circle,#a9ad9c 20%,#d8cdb5 60%,#e6dcc6)"></div>
    <div class="badge sale">-33%</div>
    <svg class="fav" width="14" height="12" viewBox="0 0 24 21"><path d="M12 20 L2.5 10.5 A5.5 5.5 0 0 1 12 3.5 A5.5 5.5 0 0 1 21.5 10.5 Z" fill="none" stroke="#333" stroke-width="1.5"/></svg>
    <div class="brand">LOREVA</div>
    <div class="name">Dessertteller NATURE COLLECTION (6 Stck.), ⌀21 cm</div>
    <div class="stock"><svg width="10" height="6" viewBox="0 0 10 6"><rect x="0" y="1" width="6" height="3.5" fill="none" stroke="#5aa83c" stroke-width=".8"/><path d="M6 2h2l1.5 1.5V4.5H6z" fill="#5aa83c"/><circle cx="2" cy="5.2" r=".8" fill="#5aa83c"/><circle cx="7.5" cy="5.2" r=".8" fill="#5aa83c"/></svg>Auf Lager</div>
    <div class="price sale">24,95 € <s>UVP 29,95 €</s></div>
    <div class="cart-btn"><svg width="11" height="10" viewBox="0 0 11 10"><path d="M0.5 1h2l1.5 5.5h5.5l1-4H3" fill="none" stroke="#fff" stroke-width="1"/><path d="M6.5 2v3M5 3.5h3" stroke="#fff" stroke-width=".9"/><circle cx="4.5" cy="8.5" r=".9" fill="#fff"/><circle cx="8.5" cy="8.5" r=".9" fill="#fff"/></svg></div>
  </article>

  <article class="card" style="left:386px;top:490px">
    <div class="thumb" role="img" aria-label="Hellblauer Teller mit goldbraunem Rand" style="background:radial-gradient(circle,#b2dce1 40%,#9fd0d8 85%,#c9a766)"></div>
    <svg class="fav" width="14" height="12" viewBox="0 0 24 21"><path d="M12 20 L2.5 10.5 A5.5 5.5 0 0 1 12 3.5 A5.5 5.5 0 0 1 21.5 10.5 Z" fill="none" stroke="#333" stroke-width="1.5"/></svg>
    <div class="brand">TIDEMOOR</div>
    <div class="name">Dessertteller NATURE COLLECTION (6 Stck.), ⌀21 cm</div>
    <div class="stock"><svg width="10" height="6" viewBox="0 0 10 6"><rect x="0" y="1" width="6" height="3.5" fill="none" stroke="#5aa83c" stroke-width=".8"/><path d="M6 2h2l1.5 1.5V4.5H6z" fill="#5aa83c"/><circle cx="2" cy="5.2" r=".8" fill="#5aa83c"/><circle cx="7.5" cy="5.2" r=".8" fill="#5aa83c"/></svg>Auf Lager</div>
    <div class="price">24,95 €</div>
    <div class="cart-btn"><svg width="11" height="10" viewBox="0 0 11 10"><path d="M0.5 1h2l1.5 5.5h5.5l1-4H3" fill="none" stroke="#fff" stroke-width="1"/><path d="M6.5 2v3M5 3.5h3" stroke="#fff" stroke-width=".9"/><circle cx="4.5" cy="8.5" r=".9" fill="#fff"/><circle cx="8.5" cy="8.5" r=".9" fill="#fff"/></svg></div>
  </article>

  <article class="card" style="left:543px;top:490px">
    <div class="thumb" role="img" aria-label="Dunkelblauer Dessertteller" style="background:radial-gradient(circle,#3a5296 30%,#253a78 80%,#1b2b5e)"></div>
    <svg class="fav" width="14" height="12" viewBox="0 0 24 21"><path d="M12 20 L2.5 10.5 A5.5 5.5 0 0 1 12 3.5 A5.5 5.5 0 0 1 21.5 10.5 Z" fill="none" stroke="#333" stroke-width="1.5"/></svg>
    <div class="brand">LOREVA</div>
    <div class="name">Dessertteller NATURE COLLECTION (6 Stck.), ⌀21 cm</div>
    <div class="stock"><svg width="10" height="6" viewBox="0 0 10 6"><rect x="0" y="1" width="6" height="3.5" fill="none" stroke="#5aa83c" stroke-width=".8"/><path d="M6 2h2l1.5 1.5V4.5H6z" fill="#5aa83c"/><circle cx="2" cy="5.2" r=".8" fill="#5aa83c"/><circle cx="7.5" cy="5.2" r=".8" fill="#5aa83c"/></svg>Auf Lager</div>
    <div class="price">24,95 €</div>
    <div class="cart-btn"><svg width="11" height="10" viewBox="0 0 11 10"><path d="M0.5 1h2l1.5 5.5h5.5l1-4H3" fill="none" stroke="#fff" stroke-width="1"/><path d="M6.5 2v3M5 3.5h3" stroke="#fff" stroke-width=".9"/><circle cx="4.5" cy="8.5" r=".9" fill="#fff"/><circle cx="8.5" cy="8.5" r=".9" fill="#fff"/></svg></div>
  </article>

  <!-- row 3 -->
  <article class="card" style="left:72px;top:697px">
    <div class="thumb" role="img" aria-label="Petrolfarbener Teller mit braunem Rand" style="width:68px;height:68px;left:39px;top:23px;background:radial-gradient(circle,#5a8284 40%,#40666a 85%,#8a5a35)"></div>
    <svg class="fav" width="14" height="12" viewBox="0 0 24 21"><path d="M12 20 L2.5 10.5 A5.5 5.5 0 0 1 12 3.5 A5.5 5.5 0 0 1 21.5 10.5 Z" fill="none" stroke="#333" stroke-width="1.5"/></svg>
    <div class="brand">TIDEMOOR</div>
    <div class="name">Dessertteller NATURE COLLECTION (6 Stck.), ⌀21 cm</div>
    <div class="stock"><svg width="10" height="6" viewBox="0 0 10 6"><rect x="0" y="1" width="6" height="3.5" fill="none" stroke="#5aa83c" stroke-width=".8"/><path d="M6 2h2l1.5 1.5V4.5H6z" fill="#5aa83c"/><circle cx="2" cy="5.2" r=".8" fill="#5aa83c"/><circle cx="7.5" cy="5.2" r=".8" fill="#5aa83c"/></svg>Auf Lager</div>
    <div class="price">24,95 €</div>
    <div class="cart-btn"><svg width="11" height="10" viewBox="0 0 11 10"><path d="M0.5 1h2l1.5 5.5h5.5l1-4H3" fill="none" stroke="#fff" stroke-width="1"/><path d="M6.5 2v3M5 3.5h3" stroke="#fff" stroke-width=".9"/><circle cx="4.5" cy="8.5" r=".9" fill="#fff"/><circle cx="8.5" cy="8.5" r=".9" fill="#fff"/></svg></div>
  </article>

  <article class="card" style="left:229px;top:697px">
    <div class="thumb" role="img" aria-label="Gestapeltes petrolfarbenes Teller- und Schalenset" style="border-radius:40%;background:radial-gradient(ellipse,#4f8783 30%,#3b6a67 70%,#fff 72%)"></div>
    <svg class="fav" width="14" height="12" viewBox="0 0 24 21"><path d="M12 20 L2.5 10.5 A5.5 5.5 0 0 1 12 3.5 A5.5 5.5 0 0 1 21.5 10.5 Z" fill="none" stroke="#333" stroke-width="1.5"/></svg>
    <div class="brand">TIDEMOOR</div>
    <div class="name">Dessert Teller Set NATURE COLLECTION (6 Stck.), ⌀21 cm</div>
    <div class="stock"><svg width="10" height="6" viewBox="0 0 10 6"><rect x="0" y="1" width="6" height="3.5" fill="none" stroke="#5aa83c" stroke-width=".8"/><path d="M6 2h2l1.5 1.5V4.5H6z" fill="#5aa83c"/><circle cx="2" cy="5.2" r=".8" fill="#5aa83c"/><circle cx="7.5" cy="5.2" r=".8" fill="#5aa83c"/></svg>Auf Lager</div>
    <div class="price">24,95 €</div>
    <div class="cart-btn"><svg width="11" height="10" viewBox="0 0 11 10"><path d="M0.5 1h2l1.5 5.5h5.5l1-4H3" fill="none" stroke="#fff" stroke-width="1"/><path d="M6.5 2v3M5 3.5h3" stroke="#fff" stroke-width=".9"/><circle cx="4.5" cy="8.5" r=".9" fill="#fff"/><circle cx="8.5" cy="8.5" r=".9" fill="#fff"/></svg></div>
  </article>

  <article class="card" style="left:386px;top:697px">
    <div class="thumb" role="img" aria-label="Beiger Dessertteller mit grüngrauem Spiegel" style="background:radial-gradient(circle,#a9ad9c 20%,#d8cdb5 60%,#e6dcc6)"></div>
    <div class="badge">NEU</div>
    <svg class="fav" width="14" height="12" viewBox="0 0 24 21"><path d="M12 20 L2.5 10.5 A5.5 5.5 0 0 1 12 3.5 A5.5 5.5 0 0 1 21.5 10.5 Z" fill="none" stroke="#333" stroke-width="1.5"/></svg>
    <div class="brand">LOREVA</div>
    <div class="name">Dessertteller NATURE COLLECTION (6 Stck.), ⌀21 cm</div>
    <div class="stock"><svg width="10" height="6" viewBox="0 0 10 6"><rect x="0" y="1" width="6" height="3.5" fill="none" stroke="#5aa83c" stroke-width=".8"/><path d="M6 2h2l1.5 1.5V4.5H6z" fill="#5aa83c"/><circle cx="2" cy="5.2" r=".8" fill="#5aa83c"/><circle cx="7.5" cy="5.2" r=".8" fill="#5aa83c"/></svg>Auf Lager</div>
    <div class="price">24,95 €</div>
    <div class="cart-btn"><svg width="11" height="10" viewBox="0 0 11 10"><path d="M0.5 1h2l1.5 5.5h5.5l1-4H3" fill="none" stroke="#fff" stroke-width="1"/><path d="M6.5 2v3M5 3.5h3" stroke="#fff" stroke-width=".9"/><circle cx="4.5" cy="8.5" r=".9" fill="#fff"/><circle cx="8.5" cy="8.5" r=".9" fill="#fff"/></svg></div>
  </article>

  <article class="card" style="left:543px;top:697px">
    <div class="thumb" role="img" aria-label="Hellblauer Teller mit goldbraunem Rand" style="background:radial-gradient(circle,#b2dce1 40%,#9fd0d8 85%,#c9a766)"></div>
    <svg class="fav" width="14" height="12" viewBox="0 0 24 21"><path d="M12 20 L2.5 10.5 A5.5 5.5 0 0 1 12 3.5 A5.5 5.5 0 0 1 21.5 10.5 Z" fill="none" stroke="#333" stroke-width="1.5"/></svg>
    <div class="brand">TIDEMOOR</div>
    <div class="name">Dessertteller NATURE COLLECTION (6 Stck.), ⌀21 cm</div>
    <div class="stock"><svg width="10" height="6" viewBox="0 0 10 6"><rect x="0" y="1" width="6" height="3.5" fill="none" stroke="#5aa83c" stroke-width=".8"/><path d="M6 2h2l1.5 1.5V4.5H6z" fill="#5aa83c"/><circle cx="2" cy="5.2" r=".8" fill="#5aa83c"/><circle cx="7.5" cy="5.2" r=".8" fill="#5aa83c"/></svg>Auf Lager</div>
    <div class="price">24,95 €</div>
    <div class="cart-btn"><svg width="11" height="10" viewBox="0 0 11 10"><path d="M0.5 1h2l1.5 5.5h5.5l1-4H3" fill="none" stroke="#fff" stroke-width="1"/><path d="M6.5 2v3M5 3.5h3" stroke="#fff" stroke-width=".9"/><circle cx="4.5" cy="8.5" r=".9" fill="#fff"/><circle cx="8.5" cy="8.5" r=".9" fill="#fff"/></svg></div>
  </article>
</main>

<nav class="pager">
  <svg width="10" height="8" viewBox="0 0 10 8"><path d="M5 1L2 4l3 3M9 1L6 4l3 3" fill="none" stroke="#2c2f7a" stroke-width="1"/></svg>
  <svg width="5" height="8" viewBox="0 0 5 8"><path d="M4 1L1 4l3 3" fill="none" stroke="#2c2f7a" stroke-width="1"/></svg>
  <span class="num">1</span><span class="num current">2</span><span class="num">3</span><span class="num">4</span><span class="num">5</span><span class="num">6</span>
  <svg width="5" height="8" viewBox="0 0 5 8"><path d="M1 1l3 3-3 3" fill="none" stroke="#2c2f7a" stroke-width="1"/></svg>
  <svg width="10" height="8" viewBox="0 0 10 8"><path d="M1 1l3 3-3 3M5 1l3 3-3 3" fill="none" stroke="#2c2f7a" stroke-width="1"/></svg>
</nav>

<footer>
  <div class="footer-ornament" role="img" aria-label="Zartes hellblaues Ornament"></div>
  <div class="newsletter-kicker">Jetzt für Newsletter anmelden</div>
  <div class="newsletter-title">Bleiben Sie informiert</div>
  <div class="newsletter-text">Lorem ipsum dolor sit amet, consetetur sadipscing elitr, sed diam nonumy.</div>
  <div class="email">E-Mail Adresse eingeben...</div>
  <div class="signup">Anmelden</div>

  <div class="foot-col" style="left:314px">
    <h3>Über uns</h3>
    <ul><li>Menüpunkt</li><li>Beispiel</li><li>Text drei Worte</li><li>Menüpunkt</li><li>Beispiel</li><li>Text drei Worte</li></ul>
  </div>
  <div class="foot-col" style="left:436px">
    <h3>Kundenservice</h3>
    <ul><li>Menüpunkt</li><li>Beispiel</li><li>Text drei Worte</li><li>Menüpunkt</li><li>Beispiel</li><li>Text drei Worte</li></ul>
  </div>
  <div class="brand-dot"></div>
  <div class="brand-mark">CERAVEL</div>

  <div class="usp-band">
    <span style="left:130px">Versandkostenfreie Lieferung ab 75 €</span>
    <span style="left:343px">Lieferung mit Parcelo &amp; Swiftra</span>
    <span style="left:531px">Sicheres &amp; zertifiziertes Shoppen</span>
  </div>
  <div class="bottom-bar"></div>
</footer>

</body>
</html>
```